Business card design Needed for new logo / Construction business, home extensions and new builds

We need a business card design using our new logo files which i will attach to this project :)

We are a small construction business specialising in home extensions, new builds and property development. We are very ambitious and would appreciate professional and elegant designs for our new business card.

Very serious about using the services on BriefNest and recently acquired our new logo from here :)

Please get involved, i will feedback when i can as i am very busy but can respond daily, thanks

Target Market(s)

People that want to build onto their houses, new building developments or adding too their existing property

Industry/Entity Type

Construction

Contact Information for Business Card

Hollin Marsh Construction, Tobias Renwick (Managing Director), Tel 07822200444, email - info@hollin-marsh, www.hollin-marsh.co.uk

Colors

Designer to choose colors to be used in the design.

Requirements
Must have
• I like a deep grey on the back please. A lot of you have provided black from and back, try mixing things up a little. The black looks cool 😎 Thanks

```html
<!DOCTYPE html>
<html lang="en">
<head>
<meta charset="utf-8">
<title>Hollin Marsh Construction – Business Card</title>
<link rel="stylesheet" href="https://fonts.googleapis.com/css2?family=Cinzel:wght@500;600&family=EB+Garamond:wght@400;500&display=swap">
<style>
  :root {
    --page: #5a5a5a;
    --card-black: #0b0b0c;
    --card-deep: #141415;
    --band-grey: #1d1d1f;
    --band-brown: #1c1710;
    --gold: #c9962e;
    --text-white: #e9e9e9;
    --pattern: #1a1a1b;
  }
  * { margin: 0; padding: 0; box-sizing: border-box; }
  html, body { width: 1200px; height: 900px; overflow: hidden; }
  body { background: var(--page); position: relative; font-family: "EB Garamond", serif; }

  .card {
    position: absolute;
    width: 620px;
    height: 354px;
    border-radius: 34px;
    overflow: hidden;
    box-shadow: 0 14px 30px rgba(0,0,0,.35);
  }

  /* Back side */
  .card-back { left: 120px; top: 60px; background: var(--card-black); }
  .card-back .pattern {
    position: absolute; inset: 0;
    background: radial-gradient(ellipse at 60% 30%, #232324 0%, var(--pattern) 45%, var(--card-black) 100%);
  }
  .card-back .back-name {
    position: absolute; right: 70px; top: 150px;
    font-family: "Cinzel", serif; font-weight: 600;
    font-size: 17px; letter-spacing: 1px; color: var(--gold);
    display: flex; align-items: center; gap: 8px;
  }
  .back-name .mark { width: 10px; height: 10px; background: var(--gold); }

  /* Front side */
  .card-front { left: 460px; top: 486px; background: var(--card-black); }
  .card-front .bands { position: absolute; inset: 0; }

  .person { position: absolute; left: 30px; top: 150px; width: 168px; }
  .person-name {
    font-family: "Cinzel", serif; font-weight: 600;
    font-size: 16px; letter-spacing: .3px; color: var(--gold); white-space: nowrap;
  }
  .person-role { font-size: 15px; color: var(--text-white); margin-top: 2px; }

  .company {
    position: absolute; left: 208px; top: 120px; width: 200px;
    text-align: center;
    font-family: "Cinzel", serif; font-weight: 600;
    color: var(--gold); font-size: 19px; line-height: 1.25; letter-spacing: .5px;
  }
  .company .mark {
    display: block; width: 14px; height: 14px; margin: 0 auto 14px;
    background: var(--gold);
  }

  .contact {
    position: absolute; right: 28px; top: 104px;
    list-style: none;
    color: var(--text-white); font-size: 14px; line-height: 1;
  }
  .contact li {
    display: flex; justify-content: flex-end; align-items: center; gap: 7px;
    height: 24px; white-space: nowrap;
  }
  .contact svg { width: 14px; height: 14px; flex: none; }
</style>
</head>
<body>

<section class="card card-back" aria-label="Card back">
  <div class="pattern" role="img" aria-label="Tonal repeating brand pattern on black"></div>
  <div class="back-name"><span class="mark"></span>Hollin Marsh</div>
</section>

<section class="card card-front" aria-label="Card front">
  <svg class="bands" viewBox="0 0 620 354" preserveAspectRatio="none" aria-hidden="true">
    <polygon points="0,0 300,0 120,354 0,354" fill="var(--card-deep)"/>
    <polygon points="250,0 420,0 300,354 160,354" fill="var(--band-grey)"/>
    <polygon points="420,0 620,0 620,120 470,80" fill="var(--band-grey)"/>
    <path d="M200,354 C260,220 420,150 620,150 L620,354 Z" fill="var(--band-brown)"/>
  </svg>

  <div class="person">
    <p class="person-name">TOBIAS RENWICK</p>
    <p class="person-role">Managing Director</p>
  </div>

  <div class="company">
    <span class="mark"></span>
    HOLLIN MARSH<br>CONSTRUCTION
  </div>

  <ul class="contact">
    <li>07822200444
      <svg viewBox="0 0 16 16"><path fill="var(--gold)" d="M4 1l3 3-2 2c1 2 3 4 5 5l2-2 3 3-2 3C7 15 1 9 1 3z"/></svg>
    </li>
    <li>info@hollin-marsh.co.uk
      <svg viewBox="0 0 16 16"><rect x="1" y="3" width="14" height="10" rx="1" fill="var(--gold)"/><path d="M1 4l7 5 7-5" stroke="#0b0b0c" stroke-width="1.3" fill="none"/></svg>
    </li>
    <li>www.hollin-marsh.co.uk
      <svg viewBox="0 0 16 16"><circle cx="8" cy="8" r="6.5" fill="none" stroke="var(--gold)" stroke-width="1.5"/><path d="M1.5 8h13M8 1.5c-3 3-3 10 0 13M8 1.5c3 3 3 10 0 13" stroke="var(--gold)" stroke-width="1.1" fill="none"/></svg>
    </li>
  </ul>
</section>

</body>
</html>
```